Redesign Website - Current one too plain

The description is in the uploaded file. Please let me know if you need any more information. I'd prefer it if someone could implement the design to a WordPress site but the best design will win, regardless.
I would like the forms to look nice as well
UPDATE:
I don't think we can use the images that I provided, I think they make the site look a bit 'cheap' and I really don't know how to replace them. One thought I have had is to make the "Simple, Unique, Effective" a second feature on the right side of the page with the search on the left
Target Market(s)
Small companies, private sellers of cars and people who rent their caravan/holiday home out
Industry/Entity Type
Advertising
Number of Pages Required
3 page
Colors
Designer to choose colors to be used in the design.
Look and feel

```html
<!DOCTYPE html>
<html lang="en">
<head>
<meta charset="utf-8">
<title>KODRA – Find an advert by its code</title>
<link rel="stylesheet" href="https://fonts.googleapis.com/css2?family=Noto+Sans:wght@400;500;600&display=swap">
<style>
  :root {
    --bg: #fdfcf6;
    --glow: rgba(250, 240, 190, 0.55);
    --ink: #1f1f1d;
    --ink-soft: #35352c;
    --text: #3c3c36;
    --muted: #8a8a84;
    --pill: #f2f1e9;
    --line: #2b2b27;
    --dark: #1e1e1e;
    --disc: #35352c;
    --white: #ffffff;
  }
  * { box-sizing: border-box; margin: 0; padding: 0; }
  html, body { width: 1200px; height: 640px; overflow: hidden; }
  body {
    position: relative;
    font-family: "Noto Sans", sans-serif;
    color: var(--ink);
    background:
      radial-gradient(circle at 180px 60px, var(--glow), transparent 170px),
      radial-gradient(circle at 625px 200px, rgba(250, 238, 185, 0.5), transparent 70px),
      radial-gradient(circle at 200px 470px, rgba(250, 242, 205, 0.35), transparent 160px),
      radial-gradient(circle at 1160px 600px, rgba(250, 240, 195, 0.45), transparent 130px),
      var(--bg);
  }

  /* Header */
  .site-header { position: absolute; left: 142px; top: 16px; width: 915px; height: 29px; }
  .brand { position: absolute; left: 0; top: 3px; display: flex; align-items: center; gap: 7px;
    font-size: 18px; font-weight: 500; letter-spacing: 0.5px; color: var(--ink); text-decoration: none; }
  .brand-dot { width: 15px; height: 15px; border-radius: 50%; background: var(--ink); }
  .main-nav { position: absolute; left: 375px; top: 6px; display: flex; gap: 25px; font-size: 11.5px; }
  .main-nav a { color: var(--ink); text-decoration: none; position: relative; }
  .main-nav a.is-active::after { content: ""; position: absolute; left: 50%; top: 19px; width: 3.5px; height: 3.5px;
    margin-left: -1.5px; border-radius: 50%; background: var(--ink); }
  .account { position: absolute; right: 0; top: 0; display: flex; align-items: center; gap: 15px; font-size: 11.5px; }
  .account a { color: var(--ink); text-decoration: none; }
  .account .login { background: var(--pill); border-radius: 15px; height: 29px; padding: 0 15px; display: flex; align-items: center; }

  /* Code picker */
  .code-picker { position: absolute; left: 215px; top: 150px; display: flex; gap: 11px; }
  .code-slot { width: 108px; display: flex; flex-direction: column; align-items: center; }
  .code-slot svg { display: block; }
  .code-char { font-size: 150px; line-height: 150px; height: 150px; margin: 14px 0 10px; font-weight: 400;
    color: var(--ink-soft); text-align: center; }

  .type-options { position: absolute; left: 142px; top: 396px; display: flex; gap: 14px; }
  .type-option { width: 115px; height: 48px; border: 1px solid var(--line); border-radius: 3px; background: transparent;
    display: flex; align-items: center; justify-content: center; gap: 8px; font-family: inherit; font-size: 13px; color: var(--ink); }
  .type-option svg { width: 13px; height: 13px; }

  .search-btn { position: absolute; left: 231px; top: 476px; width: 195px; height: 42px; border: 0; border-radius: 21px;
    background: var(--dark); color: var(--white); font-family: inherit; font-size: 14px; font-weight: 500; letter-spacing: 0.3px; }

  /* Features */
  .feature { position: absolute; width: 200px; }
  .feature-title { display: flex; align-items: center; gap: 11px; font-size: 22.5px; font-weight: 400; color: var(--ink); }
  .feature-title svg { width: 24px; height: 24px; flex: none; }
  .feature p { margin-top: 10px; padding-left: 37px; font-size: 13px; line-height: 17.5px; color: var(--text); }
  .feature-simple { left: 627px; top: 206px; }
  .feature-unique { left: 861px; top: 206px; }
  .feature-unique p { padding-left: 35px; }
  .feature-effective { left: 627px; top: 313px; }
  .feature-effective .feature-title { gap: 7px; }

  .advertise-cta { position: absolute; left: 917px; top: 313px; width: 140px; height: 140px; border-radius: 50%;
    background: var(--disc); color: var(--white); display: flex; align-items: center; justify-content: center; text-align: center;
    font-size: 13.5px; font-weight: 600; line-height: 19.5px; letter-spacing: 0.4px; text-decoration: none;
    box-shadow: 0 10px 30px rgba(245, 228, 160, 0.45); }

  /* Footer */
  .site-footer { position: absolute; left: 142px; top: 609px; width: 915px; font-size: 11.5px; color: var(--muted); }
  .legal { position: absolute; right: 0; top: 0; display: flex; align-items: center; gap: 10px; }
  .legal a { color: var(--muted); text-decoration: none; }
  .legal .sep { width: 1px; height: 8px; background: var(--muted); }
</style>
</head>
<body>
  <header class="site-header">
    <a class="brand" href="#"><span class="brand-dot"></span>KODRA</a>
    <nav class="main-nav">
      <a class="is-active" href="#">Home</a>
      <a href="#">Advertise</a>
      <a href="#">Contact</a>
    </nav>
    <div class="account">
      <a href="#">Register</a>
      <a class="login" href="#">Login</a>
    </div>
  </header>

  <main>
    <section class="code-picker" aria-label="Advert code">
      <div class="code-slot">
        <svg width="26" height="16" viewBox="0 0 26 16"><path d="M2 14 L13 3 L24 14" fill="none" stroke="#35352c" stroke-width="3"/></svg>
        <div class="code-char">A</div>
        <svg width="26" height="16" viewBox="0 0 26 16"><path d="M2 2 L13 13 L24 2" fill="none" stroke="#35352c" stroke-width="3"/></svg>
      </div>
      <div class="code-slot">
        <svg width="26" height="16" viewBox="0 0 26 16"><path d="M2 14 L13 3 L24 14" fill="none" stroke="#35352c" stroke-width="3"/></svg>
        <div class="code-char">1</div>
        <svg width="26" height="16" viewBox="0 0 26 16"><path d="M2 2 L13 13 L24 2" fill="none" stroke="#35352c" stroke-width="3"/></svg>
      </div>
    </section>

    <div class="type-options">
      <button class="type-option" type="button">
        <svg viewBox="0 0 16 16"><path d="M3 7 L4.5 3 H11.5 L13 7 H14 V12 H12.5 V14 H10.5 V12 H5.5 V14 H3.5 V12 H2 V7 Z" fill="#1f1f1d"/><circle cx="5" cy="9.3" r="1.1" fill="#fff"/><circle cx="11" cy="9.3" r="1.1" fill="#fff"/><path d="M4.6 7 L5.4 4.5 H10.6 L11.4 7 Z" fill="#fff"/></svg>
        car
      </button>
      <button class="type-option" type="button">
        <svg viewBox="0 0 16 16"><rect x="1" y="3.5" width="13" height="8" rx="1.5" fill="#1f1f1d"/><rect x="3" y="5.5" width="4" height="2.5" fill="#fff"/><rect x="9" y="5.5" width="3" height="4" fill="#fff"/><circle cx="5" cy="12.5" r="1.8" fill="#1f1f1d"/><rect x="14" y="9.5" width="2" height="1.2" fill="#1f1f1d"/></svg>
        caravan
      </button>
      <button class="type-option" type="button">
        <svg viewBox="0 0 16 16"><path d="M5.5 4 V2.5 H10.5 V4" fill="none" stroke="#1f1f1d" stroke-width="1.5"/><rect x="1" y="4" width="14" height="10" rx="1.5" fill="#1f1f1d"/><rect x="1" y="8" width="14" height="1" fill="#fff"/><rect x="7" y="7" width="2" height="3" fill="#fff"/></svg>
        company
      </button>
    </div>

    <button class="search-btn" type="button">Search</button>

    <section class="feature feature-simple">
      <h2 class="feature-title">
        <svg viewBox="0 0 24 24"><path d="M9 6 C9.6 10 10.5 11 14.5 12 C10.5 13 9.6 14 9 18 C8.4 14 7.5 13 3.5 12 C7.5 11 8.4 10 9 6 Z" fill="none" stroke="#1f1f1d" stroke-width="1.6" stroke-linejoin="round"/><path d="M18 1.5 C18.3 3.5 18.7 3.9 20.5 4.2 C18.7 4.5 18.3 5 18 7 C17.7 5 17.3 4.5 15.5 4.2 C17.3 3.9 17.7 3.5 18 1.5 Z" fill="#1f1f1d"/><path d="M18 16 C18.3 18 18.7 18.4 20.5 18.7 C18.7 19 18.3 19.5 18 21.5 C17.7 19.5 17.3 19 15.5 18.7 C17.3 18.4 17.7 18 18 16 Z" fill="#1f1f1d"/></svg>
        Simple
      </h2>
      <p>create your advert and display your code</p>
    </section>

    <section class="feature feature-unique">
      <h2 class="feature-title">
        <svg viewBox="0 0 24 24"><g stroke="#1f1f1d" stroke-width="2.4" stroke-linecap="round"><path d="M12 2 V22"/><path d="M2 12 H22"/><path d="M5 5 L19 19"/><path d="M19 5 L5 19"/></g></svg>
        Unique
      </h2>
      <p>customers find you by an easy-to-remember code</p>
    </section>

    <section class="feature feature-effective">
      <h2 class="feature-title">
        <svg viewBox="0 0 24 24"><g fill="none" stroke="#1f1f1d" stroke-width="1.8" stroke-linecap="round" stroke-linejoin="round"><path d="M12 2 V10"/><path d="M9.5 4.5 L12 2 L14.5 4.5"/><path d="M2 11 H9"/><path d="M4.5 8.5 L2 11 L4.5 13.5"/><path d="M15 11 H22"/><path d="M19.5 8.5 L22 11 L19.5 13.5"/><path d="M12 10 C12 14 9 14 9 18"/><circle cx="9" cy="20" r="2"/></g></svg>
        Effective
      </h2>
      <p>customers are directed to you and not a list of your competitors</p>
    </section>

    <a class="advertise-cta" href="#">ADVERTISE<br>YOUR<br>COMPANY</a>
  </main>

  <footer class="site-footer">
    <span>Copyright © 2023 kodra.com</span>
    <div class="legal">
      <a href="#">Terms of service</a>
      <span class="sep"></span>
      <a href="#">Privacy</a>
    </div>
  </footer>
</body>
</html>
```